Need a landing page design.

We are currently trying to develop a landing page for our www.brightoakwellness.example website.

Objective: To peak a level of interest in Medical Practices to sign up to our program and promote our line of vitamins and supplements. We will be concentrating on email marketing as well as fax or direct mail to drive medical facilities to our landing page.

Page requirements:
1. A slider on the top portion showing our line of products from the brightoakwellness.example website.
2. An "about us" area to explain who we are and what we offer.
3. An area for a grid so that we can show potential earnings for the practice as part of our program.
4. A Testimonial area for a couple of testimonials
5. A scroll area where they can see our contract
6. A lead capture area where they can input their contact information so we may gather it and contact them back to explain the program. In this area I need the following fields: Name of Practice; Contact name; Email address; Phone Number; Area of Medical Discipline; Number of patients per day.
7. A nice clean contact us area

Other than these main requirements the rest is up to you.

Goal: Entice Medical practices to use our FREE service to increase revenue for their offices while helping their patients save money on their supplements.

Key Factors for the Medical facility to know: Free to sign up, no inventory carrying costs. Simple backend sales area to process orders. We handle all shipping and customer service.

Thank you

Target Market(s)

Medical Facilities, mainly office managers and docotors

Industry/Entity Type

Marketing

Requirements
Must have
• Professional design as we are dealing with the medical field.

```html
<!DOCTYPE html>
<html lang="en">
<head>
<meta charset="utf-8">
<title>Bright Oak Wellness – Practice Program</title>
<link rel="stylesheet" href="https://fonts.googleapis.com/css2?family=Ubuntu:wght@400;500&family=Open+Sans:ital,wght@0,400;0,600;1,400&display=swap">
<style>
:root{
  --brown:#6b5039;
  --brown-dark:#4e3a29;
  --teal:#6fc8d0;
  --teal-dark:#4fb3bd;
  --blue:#3a7bc2;
  --ink:#3a3a3a;
  --muted:#5c5c5c;
  --band:#efefef;
  --white:#fff;
}
*{box-sizing:border-box;margin:0;padding:0}
html,body{width:693px;height:1200px;overflow:hidden}
body{position:relative;background:#fbfbfb;font-family:"Open Sans",sans-serif;color:var(--ink)}
.abs{position:absolute}

.topbar{left:0;top:0;width:693px;height:27px;background:var(--brown);color:#fff;font-family:"Ubuntu",sans-serif;font-size:8px}
.topbar .links{left:70px;top:10px}
.topbar .links span{margin:0 5px}
.topbar .cart{right:77px;top:8px;display:flex;align-items:center;gap:6px}

.brand{left:69px;top:32px;display:flex;align-items:center;gap:8px}
.brand .dot{width:67px;height:67px;border-radius:50%;background:var(--teal);border:4px solid #d9cfc4}
.brand .name{font-family:"Ubuntu",sans-serif;font-size:13px;color:var(--brown);line-height:1.15;width:70px}
.inquiries{right:70px;top:54px;text-align:right;font-family:"Ubuntu",sans-serif;color:#444}
.inquiries .t{font-size:13px;font-weight:500}
.inquiries .p{font-size:14px;margin-top:3px}

.nav{left:69px;top:104px;width:554px;height:38px;background:var(--teal);display:flex;align-items:center;padding-left:14px;font-family:"Ubuntu",sans-serif;font-size:10px;color:#fff;gap:13px}
.nav .signin{position:absolute;right:6px;top:10px;background:var(--brown);padding:3px 10px;font-size:10px}

.slider{left:69px;top:146px;width:554px;height:145px;background:var(--blue)}
.slider .slogan{left:0;width:114px;top:18px;text-align:right;font-family:"Ubuntu",sans-serif;font-size:19px;font-weight:500;color:#fff;line-height:28px}
.slider ul{list-style:none;left:127px;top:22px;color:#fff;font-family:"Ubuntu",sans-serif;font-size:8.5px}
.slider li{height:22.3px;display:flex;align-items:center;gap:9px}
.slider li i{width:10px;height:10px;border-radius:50%;background:#fff;display:inline-block}
.slider .product{left:273px;top:12px;width:135px;height:120px;border-radius:8px;background:linear-gradient(135deg,#2a8fd0,#1a5e9a)}
.slider .shop{left:453px;top:92px;background:var(--brown);color:#fff;font-family:"Ubuntu",sans-serif;font-size:10px;padding:5px 12px}
.slider .dots{left:490px;top:123px;display:flex;gap:3px}
.slider .dots i{width:7px;height:7px;border-radius:50%;background:#fff}
.slider .dots i:last-child{background:var(--teal)}

.section-title{font-family:"Ubuntu",sans-serif;font-size:12.5px;font-weight:500;color:#3a3a3a}
.about{left:75px;top:308px;width:358px}
.about h3{font-family:"Ubuntu",sans-serif;font-size:10px;font-weight:500;margin:16px 0 9px}
.about p{font-size:7.3px;line-height:13.8px;color:var(--muted);text-align:justify}

.quick-title{left:444px;top:307px}
.quick{left:444px;top:333px;width:173px;height:196px;background:linear-gradient(#6e533b,#5a4330);border-radius:2px;padding:9px 13px}
.quick .field{height:18px;margin-bottom:8.3px;background:rgba(255,255,255,.22);border:1px solid rgba(255,255,255,.25);border-radius:2px;font-size:5.8px;color:#a88c72;padding:5px 6px}
.quick .submit{margin:4px auto 0;width:69px;height:17px;background:#2c2723;color:#fff;font-family:"Ubuntu",sans-serif;font-size:9px;text-align:center;line-height:17px}

.band{left:0;top:574px;width:693px;height:224px;background:var(--band)}
.products-title{left:75px;top:584px}
.product-card{top:612px;width:104px}
.product-card .img{margin-left:24px;width:56px;height:82px;border-radius:6px}
.product-card p{font-size:6.2px;line-height:12.6px;font-weight:600;color:#444;margin-top:10px}
.product-card .row{display:flex;justify-content:space-between;align-items:center;margin-top:3px;padding-bottom:6px;border-bottom:1px solid #ddd}
.product-card .price{font-family:"Ubuntu",sans-serif;font-size:10px;font-weight:500;color:#333}
.product-card .cart{background:var(--teal);color:#fff;font-size:6.3px;font-weight:600;padding:5px 3px}
.product-card .stars{font-size:8.5px;margin-top:3px;color:#444;letter-spacing:-.5px}
.product-card .stars b{color:var(--teal);font-weight:400}

.earn{left:444px;top:574px;width:180px;height:224px;background:#f6f6f6}
.earn .section-title{margin:10px 0 0 13px;line-height:19px}
.earn .photo{margin:4px 0 0 15px;width:151px;height:98px;border:3px solid #fff;box-shadow:0 0 0 1px #ddd;background:linear-gradient(90deg,#5c8f3c,#e8e0d2 50%,#9a6a3b)}
.earn p{margin:8px 0 0 15px;width:150px;font-size:6.7px;line-height:14px;color:#444}
.earn p span{color:var(--teal)}

.testi-title{left:74px;top:838px}
.testi{top:866px;width:170px}
.testi .q{font-family:Georgia,serif;font-size:13px;font-weight:700;color:#444;line-height:10px}
.testi p{font-style:italic;font-size:6.6px;line-height:13.8px;color:var(--muted);text-align:justify;padding-left:4px}
.testi .who{font-family:"Ubuntu",sans-serif;font-size:10px;color:#2a8c94;margin:10px 0 0 4px}
.testi .role{font-size:6px;color:#222;margin:2px 0 0 4px}

.contract{left:443px;top:829px;width:172px;height:156px;background:linear-gradient(#79cdd5,#5dbcc7);padding:9px 10px}
.contract h2{font-family:"Ubuntu",sans-serif;font-size:12px;font-weight:400;color:#fff}
.contract .scroll{position:relative;margin-top:14px;height:108px;background:rgba(255,255,255,.06)}
.contract p{font-size:6.1px;line-height:13.8px;color:#fff;width:135px;text-align:justify}
.contract .bar{position:absolute;right:0;top:0;width:8px;height:108px;background:#fff;border-radius:4px}
.contract .thumb{position:absolute;right:1px;top:1px;width:6px;height:22px;background:var(--brown-dark);border-radius:3px;border:1px solid #fff}

.footer{left:0;top:1010px;width:693px;height:148px;background:var(--brown);color:#fff}
.footer h4{position:absolute;top:19px;font-family:"Ubuntu",sans-serif;font-size:7.5px;font-weight:400}
.footer ul{position:absolute;top:43px;list-style:none;font-size:6.3px;line-height:13.8px}
.footer .news{position:absolute;left:252px;top:40px;width:116px;font-size:6.2px;line-height:13px}
.footer .news .in{height:16px;background:#fff;margin-top:7px;border:1px solid #ccc;color:#999;font-size:5.8px;padding:4px 3px}
.footer .news .btn{margin:8px 0 0 2px;width:57px;height:13px;background:var(--teal);border-radius:7px;font-size:6.3px;text-align:center;line-height:13px}
.footer .row{position:absolute;display:flex;align-items:center;font-size:6.3px}
.footer .ic{width:12px;height:12px;border-radius:50%;background:var(--teal)}
.bottom{left:0;top:1158px;width:693px;height:42px;background:var(--brown);border-top:1px solid #5f4732;color:#fff;font-size:6.6px;padding:21px 0 0 80px}
</style>
</head>
<body>

<header>
  <div class="abs topbar">
    <div class="abs links">My Account<span>|</span>Checkout<span>|</span>Log in</div>
    <div class="abs cart">Shopping Cart
      <svg width="15" height="12" viewBox="0 0 15 12" fill="none" stroke="#fff" stroke-width="1"><path d="M0 1h3l2 7h8l1.5-5H4"/><circle cx="6" cy="10.5" r="1"/><circle cx="12" cy="10.5" r="1"/></svg>
      (0 Items)
    </div>
  </div>

  <div class="abs brand"><div class="dot"></div><div class="name">Bright Oak Wellness</div></div>
  <div class="abs inquiries"><div class="t">General Inquiries</div><div class="p">(555) 274-0154</div></div>

  <nav class="abs nav"><span>Home</span><span>About Us</span><span>Products</span><span>Contact Us</span><span class="signin">SIGN IN</span></nav>
</header>

<section class="abs slider">
  <div class="abs slogan">THINK<br>ACT<br>CONQUER</div>
  <ul class="abs">
    <li><i></i>Help Promote Memory</li>
    <li><i></i>Mental Energy (ATP)</li>
    <li><i></i>Motivation</li>
    <li><i></i>Oxygen Levels to the Brain</li>
    <li><i></i>Verbal Fluency</li>
  </ul>
  <div class="abs product" role="img" aria-label="Product photo of blue supplement bottles"></div>
  <div class="abs shop">SHOP NOW</div>
  <div class="abs dots"><i></i><i></i><i></i><i></i></div>
</section>

<section class="abs about">
  <h2 class="section-title">ABOUT US</h2>
  <h3>What We Do ?</h3>
  <p>Lorem ipsum dolor sit amet, consectetur adipisicing elit, sed do eiusmod tempor incididunt ut labore et dolore magna aliqua. Ut enim ad minim veniam, quis nostrud exercitation ullamco laboris nisi ut aliquip ex ea commodo consequat. Duis aute irure dolor in reprehenderit in voluptate velit esse cillum dolore eu fugiat nulla pariatur. Excepteur sint occaecat cupidatat non proident, sunt in culpa qui officia deserunt mollit anim id est laborum.</p>
  <h3>What We Offer ?</h3>
  <p>Lorem ipsum dolor sit amet, consectetur adipisicing elit, sed do eiusmod tempor incididunt ut labore et dolore magna aliqua. Ut enim ad minim veniam, quis nostrud exercitation ullamco laboris nisi ut aliquip ex ea commodo consequat. Duis aute irure dolor in reprehenderit in voluptate velit esse cillum dolore eu fugiat nulla pariatur. Excepteur sint occaecat cupidatat non proident, sunt in culpa qui officia deserunt mollit anim id est laborum.</p>
</section>

<h2 class="abs section-title quick-title">QUICK CONTACT</h2>
<form class="abs quick">
  <div class="field">Name of Practice</div>
  <div class="field">Contact name</div>
  <div class="field">Email address</div>
  <div class="field">Phone Number</div>
  <div class="field">Area of Medical Discipline</div>
  <div class="field">Number of patients per day</div>
  <div class="submit">SUBMIT</div>
</form>

<div class="abs band"></div>
<h2 class="abs section-title products-title">PRODUCTS</h2>
<div class="abs product-card" style="left:75px">
  <div class="img" role="img" aria-label="Dark supplement bottle" style="background:linear-gradient(#2b2f45,#11131f)"></div>
  <p>Consectetur adipisicing elit, do quis nostrud exercitation</p>
  <div class="row"><span class="price">$268.00</span><span class="cart">ADD TO CART</span></div>
  <div class="stars"><b>★★★</b>★★</div>
</div>
<div class="abs product-card" style="left:199px">
  <div class="img" role="img" aria-label="White supplement tub" style="background:linear-gradient(#f2f2f2,#b9a68e)"></div>
  <p>Consectetur adipisicing elit, do quis nostrud exercitation</p>
  <div class="row"><span class="price">$268.00</span><span class="cart">ADD TO CART</span></div>
  <div class="stars"><b>★★★</b>★★</div>
</div>
<div class="abs product-card" style="left:322px">
  <div class="img" role="img" aria-label="Blue supplement bottle" style="background:linear-gradient(#2d93d4,#1b5f9b)"></div>
  <p>Consectetur adipisicing elit, do quis nostrud exercitation</p>
  <div class="row"><span class="price">$268.00</span><span class="cart">ADD TO CART</span></div>
  <div class="stars"><b>★★★</b>★★</div>
</div>

<section class="abs earn">
  <h2 class="section-title">POTENTIAL EARNINGS FOR THE PRACTICE</h2>
  <div class="photo" role="img" aria-label="Supplement tub surrounded by natural ingredients"></div>
  <p>Lorem Ipsum is simply dummy text of the printing and typesetting industry. Lorem Ipsum has been the industry's standard dummy text ever... <span>Read More</span></p>
</section>

<h2 class="abs section-title testi-title">TESTIMONIALS</h2>
<div class="abs testi" style="left:73px">
  <div class="q">“</div>
  <p>Lorem ipsum dolor sit amet, consectetur adipisicing elit, sed do eiusmod tempor incididunt ut labore et dolore magna aliqua. Ut enim ad minim veniam, quis nostrud exercitation ullamco laboris nisi ut aliquip ex ea commodo consequat. <b class="q">”</b></p>
  <div class="who">Daniel Mercer</div><div class="role">Executive Market Head</div>
</div>
<div class="abs testi" style="left:258px">
  <div class="q">“</div>
  <p>Lorem ipsum dolor sit amet, consectetur adipisicing elit, sed do eiusmod tempor incididunt ut labore et dolore magna aliqua. Ut enim ad minim veniam, quis nostrud exercitation ullamco laboris nisi ut aliquip ex ea commodo consequat. <b class="q">”</b></p>
  <div class="who">Aaron Whitley</div><div class="role">Executive Market Head</div>
</div>

<section class="abs contract">
  <h2>Our Contract</h2>
  <div class="scroll">
    <p>Lorem ipsum dolor sit amet, consectetur adipisicing elit, sed do eiusmod tempor incididunt ut labore et dolore magna aliqua. Ut enim ad minim veniam, quis nostrud exercitation ullamco laboris nisi ut aliquip ex ea commodo consequat.<br>Lorem ipsum dolor sit amet, consectetur adipisicing elit, sed do eiusmod .</p>
    <div class="bar"></div><div class="thumb"></div>
  </div>
</section>

<footer class="abs footer">
  <h4 style="left:80px">Menu Links</h4>
  <ul style="left:78px"><li>Home</li><li>About Us</li><li>Products</li><li>Contact Us</li></ul>
  <h4 style="left:160px">Support Links</h4>
  <ul style="left:159px"><li>Legal Notice</li><li>Privacy Policy</li><li>Terms &amp; Conditions</li><li>Help</li></ul>
  <h4 style="left:252px">Newsletter SignUp</h4>
  <div class="news">Sign-up for our daily emails by entering your information below:
    <div class="in">Name</div><div class="in">Enter Your E-Mail ID</div>
    <div class="btn">Subscribe</div>
  </div>
  <h4 style="left:391px">Connect With Us</h4>
  <div class="row" style="left:390px;top:44px;width:85px;justify-content:space-between">Newsfeed<span class="ic"></span></div>
  <div class="row" style="left:390px;top:65px;width:85px;justify-content:space-between">Community<span class="ic"></span></div>
  <div class="row" style="left:390px;top:84px;width:85px;justify-content:space-between">Network<span class="ic"></span></div>
  <h4 style="left:495px">Contact Us</h4>
  <div class="row" style="left:494px;top:44px;gap:8px">
    <svg width="9" height="10" viewBox="0 0 9 10"><path d="M1 1l2-1 1.5 2.5-1 1c.5 1.3 1.5 2.3 2.8 2.8l1-1L9 7.5 8 9.5C4 9 1 6 .5 2z" fill="#6fc8d0"/></svg>1-555-928-2028</div>
  <div class="row" style="left:494px;top:66px;gap:8px">
    <svg width="10" height="7" viewBox="0 0 10 7" fill="none" stroke="#6fc8d0"><rect x=".5" y=".5" width="9" height="6"/><path d="M.5.5l4.5 3.5 4.5-3.5"/></svg>info@brightoakwellness.example</div>
  <div class="row" style="left:494px;top:85px;gap:8px">
    <svg width="10" height="9" viewBox="0 0 10 9" fill="none" stroke="#6fc8d0"><rect x=".5" y=".5" width="9" height="6"/><path d="M3 8.5h4"/></svg>www.brightoakwellness.example</div>
</footer>
<div class="abs bottom">Copyright ©2013 Company Name &nbsp; - All rights reserved</div>

</body>
</html>
```